Current website re-design to a updated look and feel.

We currently have a website www.brightlanefreight.com that we want to give an updated look and feel to. We are a logistics company that competes with Harbex, Dm Whitfield, Tarn but on a smaller scale. We want something fresh and updated. We have two locations one in downtown Chicago, IL and one in Palatine IL. We are a fun group that also gets the job done. We know we need pictures of both locations and possibly a video, but we need fresh design ideas. The 'who we are' page is really the only page that we currently want to keep. The 'what we do' page needs to be completely re-done from a look and feel for sure.

Target Market(s)

Anyone who uses Truck transportation to move their product. Mainly US manufacturers.

Industry/Entity Type

Logistics

Number of Pages Required

5+ page

Font styles to use
Sans Serif

Colors
5c91c4
0355a3
d0dfed

Requirements
Must have
• The new design must entice people to want to do business with us. The design must have locations for pictures and at least one video which we know we will have to provide. Design must be easy to navigate.

```html
<!DOCTYPE html>
<html lang="en">
<head>
<meta charset="utf-8">
<title>Bright Lane Freight</title>
<link rel="stylesheet" href="https://fonts.googleapis.com/css2?family=Source+Sans+3:wght@400;600;700&display=swap">
<style>
  :root {
    --blue: #0355a3;
    --blue-light: #5c91c4;
    --blue-pale: #d0dfed;
    --white: #ffffff;
    --ink: #1f2328;
    --muted: #555a60;
    --section-grey: #efefef;
    --section-soft: #f4f4f6;
  }
  * { margin: 0; padding: 0; box-sizing: border-box; }
  html, body { width: 1200px; height: 2416px; overflow: hidden; }
  body {
    position: relative;
    font-family: "Source Sans 3", Arial, sans-serif;
    color: var(--ink);
    background: var(--section-soft);
  }
  .abs { position: absolute; }

  /* Header */
  .site-header { left: 0; top: 0; width: 1200px; height: 80px; background: var(--blue); }
  .brand { left: 0; top: 0; width: 304px; height: 80px; background: var(--white);
    display: flex; align-items: center; gap: 12px; padding-left: 34px; }
  .brand-mark { width: 22px; height: 22px; border-radius: 50%; background: var(--blue); }
  .brand-name { font-size: 30px; font-weight: 600; color: var(--blue); }
  .main-nav { left: 325px; top: 0; height: 80px; display: flex; align-items: center; gap: 25px; }
  .main-nav a { color: var(--white); text-decoration: none; font-size: 16px; font-weight: 600;
    display: flex; align-items: center; gap: 5px; }
  .btn-outline { border: 2px solid var(--white); border-radius: 4px; color: var(--white);
    display: flex; align-items: center; justify-content: center; font-weight: 600; text-decoration: none; }
  .login { left: 1067px; top: 21px; width: 69px; height: 40px; font-size: 16px; }

  /* Hero */
  .hero { left: 0; top: 80px; width: 1200px; height: 601px;
    background: linear-gradient(180deg, #6d7a8c 0%, #c99a72 30%, #6a6258 52%, #3d3f44 75%, #2b2d31 100%); }
  .hero-copy { left: 0; top: 430px; width: 1200px; text-align: center; color: var(--white);
    text-shadow: 0 2px 6px rgba(0,0,0,.55); }
  .hero-title { font-size: 72px; font-weight: 700; line-height: 1; }
  .hero-sub { margin-top: 30px; font-size: 30px; font-weight: 600; line-height: 44px; }

  /* Quote band */
  .quote-band { left: 0; top: 681px; width: 1200px; height: 168px; background: var(--blue); color: var(--white); }
  .quote-title { left: 204px; top: 30px; font-size: 47px; font-weight: 700; }
  .quote-sub { left: 204px; top: 92px; font-size: 26px; font-weight: 600; }
  .quote-btn { left: 832px; top: 63px; width: 160px; height: 40px; font-size: 16px; }

  /* What we do */
  .services { left: 0; top: 849px; width: 1200px; height: 981px; background: var(--section-grey); }
  .section-title { width: 1200px; left: 0; text-align: center; color: var(--blue); font-weight: 700; }
  .services .section-title { top: 48px; font-size: 46px; }
  .card { top: 141px; width: 360px; height: 499px; background: var(--white); }
  .card-photo { width: 100%; height: 240px; }
  .card h3 { margin: 18px 0 0 22px; font-size: 21px; font-weight: 700; letter-spacing: .3px; }
  .card p { margin: 14px 22px 0 22px; font-size: 16px; line-height: 23px; color: var(--muted); }
  .btn-blue-outline { border: 2px solid var(--blue); border-radius: 4px; color: var(--blue);
    font-size: 16px; font-weight: 600; text-decoration: none; display: flex; align-items: center; justify-content: center;
    width: 104px; height: 40px; }
  .card .btn-blue-outline { position: absolute; right: 16px; }

  .carriers { left: 40px; top: 681px; width: 1119px; height: 239px; }
  .carriers-photo { left: 0; top: 0; width: 359px; height: 239px;
    background: linear-gradient(135deg, #d9dde2 0%, #9aa2ac 50%, #5b626b 100%); }
  .carriers-panel { left: 359px; top: 0; width: 760px; height: 239px; background: var(--blue);
    color: var(--white); text-align: center; }
  .carriers-panel h3 { margin-top: 38px; font-size: 21px; font-weight: 700; }
  .carriers-panel .lead { margin-top: 14px; font-size: 16px; font-weight: 700; }
  .carriers-panel p { font-size: 16px; line-height: 24px; }
  .carriers-panel .btn-outline { width: 104px; height: 40px; margin: 16px auto 0; font-size: 16px; }

  /* Vision */
  .vision { left: 0; top: 1830px; width: 1200px; height: 586px; background: var(--section-soft); }
  .vision .section-title { top: 46px; font-size: 49px; }
  .video { left: 40px; top: 157px; width: 525px; height: 353px; box-shadow: 0 3px 8px rgba(0,0,0,.35); }
  .video-frame { width: 525px; height: 325px;
    background: linear-gradient(180deg, #57606e 0%, #c48b63 30%, #5c5a57 55%, #36383d 100%); }
  .video-controls { width: 525px; height: 28px; background: linear-gradient(#e9e9e9, #c9c9c9);
    display: flex; align-items: center; font-size: 12px; color: #222; }
  .ctrl { height: 28px; display: flex; align-items: center; justify-content: center; border-right: 1px solid #aaa; }
  .ctrl-play { width: 34px; }
  .ctrl-time { width: 88px; }
  .ctrl-track { flex: 1; padding: 0 12px; border-right: 1px solid #aaa; }
  .track { width: 100%; height: 4px; background: #9a9a9a; border-radius: 2px; position: relative; }
  .track-fill { position: absolute; left: 0; top: 0; height: 4px; width: 43%; background: var(--blue); border-radius: 2px; }
  .ctrl-icon { width: 34px; }
  .ctrl-icon:last-child { border-right: none; }
  .vision-text { left: 630px; top: 231px; width: 515px; font-size: 16px; line-height: 27.5px; color: var(--ink); }
</style>
</head>
<body>

<header class="site-header abs">
  <div class="brand abs">
    <span class="brand-mark"></span>
    <span class="brand-name">Bright Lane</span>
  </div>
  <nav class="main-nav abs">
    <a href="#">WHAT WE DO</a>
    <a href="#">HOW WE DO IT</a>
    <a href="#">WHO WE ARE</a>
    <a href="#">TRACKING</a>
    <a href="#"><svg width="16" height="15" viewBox="0 0 16 15" aria-hidden="true"><path d="M1.5 1.5h13v9h-9l-4 3z" fill="none" stroke="#fff" stroke-width="1.6" stroke-linejoin="round"/></svg>CHAT</a>
    <a href="#">CONTACT</a>
  </nav>
  <a class="btn-outline login abs" href="#">Login</a>
</header>

<section class="hero abs" role="img" aria-label="Highway at sunset lined with office buildings, light trails of traffic and a central street lamp"></section>
<div class="hero-copy abs">
  <h1 class="hero-title">Relax. We Got This.</h1>
  <p class="hero-sub">Cost effective solutions for warehousing and<br>distribution of your products in every situation.</p>
</div>

<section class="quote-band abs">
  <h2 class="quote-title abs">You Are Shipping With Care</h2>
  <p class="quote-sub abs">REQUEST A QUOTE NOW TO BEGIN YOUR DELIVERY!</p>
  <a class="btn-outline quote-btn abs" href="#">REQUEST A QUOTE</a>
</section>

<section class="services abs">
  <h2 class="section-title abs">What We Do</h2>

  <article class="card abs" style="left:40px">
    <div class="card-photo" role="img" aria-label="Container port with stacked shipping containers and cranes" style="background:linear-gradient(180deg,#8d98a6 0%,#6e7a86 40%,#4f6a6a 70%,#3f4c52 100%)"></div>
    <h3>FREIGHT MANAGEMENT</h3>
    <p>We strive for a perfect delivery and promise to be there for anything you may need, every step of the way.</p>
    <a class="btn-blue-outline" href="#" style="top:384px;right:16px">Learn More</a>
  </article>

  <article class="card abs" style="left:419px">
    <div class="card-photo" role="img" aria-label="Red semi truck with white trailer on an open road under a bright sky" style="background:linear-gradient(180deg,#9bb3cc 0%,#dfe5ea 45%,#a8322f 62%,#5c6166 100%)"></div>
    <h3>TRANSPORTATION</h3>
    <p>With a combined 500+ years of industry experience between all employees, we are the logistics company you need to get the job done right</p>
    <a class="btn-blue-outline" href="#" style="top:412px">Learn More</a>
  </article>

  <article class="card abs" style="left:799px">
    <div class="card-photo" role="img" aria-label="Warehouse shelving stocked with cardboard boxes" style="background:linear-gradient(180deg,#b89b72 0%,#d9b98a 45%,#c29862 75%,#a57a46 100%)"></div>
    <h3>WAREHOUSE &amp; DISTRIBUTION</h3>
    <p style="color:var(--ink)">Our secure facility can accommodate large or small quantities of product. Our inventory management system provides real-time visibility.</p>
    <a class="btn-blue-outline" href="#" style="top:434px">Learn More</a>
  </article>

  <div class="carriers abs">
    <div class="carriers-photo abs" role="img" aria-label="Truck driver holding a clipboard in front of a row of white trucks"></div>
    <div class="carriers-panel abs">
      <h3>CARRIERS</h3>
      <p class="lead">Are you a carrier looking to work with Bright Lane?</p>
      <p>Find out why we have the best carrier relationships in the business.</p>
      <a class="btn-outline" href="#">Learn More</a>
    </div>
  </div>
</section>

<section class="vision abs">
  <h2 class="section-title abs">Bright Lane Transportation Vision And Mission</h2>

  <div class="video abs">
    <div class="video-frame" role="img" aria-label="Video still of a highway at sunset beside office buildings"></div>
    <div class="video-controls">
      <div class="ctrl ctrl-play"><svg width="12" height="13" viewBox="0 0 12 13" aria-hidden="true"><path d="M1 0.5l10 6-10 6z" fill="#111"/></svg></div>
      <div class="ctrl ctrl-time">02:00/05:03</div>
      <div class="ctrl-track"><div class="track"><div class="track-fill"></div></div></div>
      <div class="ctrl ctrl-icon"><svg width="18" height="14" viewBox="0 0 18 14" aria-hidden="true"><path d="M1 4.5h3.5L9 1v12L4.5 9.5H1z" fill="#111"/><path d="M11.5 4.5a3 3 0 0 1 0 5M13.5 2.5a6 6 0 0 1 0 9" fill="none" stroke="#111" stroke-width="1.5"/></svg></div>
      <div class="ctrl ctrl-icon"><svg width="13" height="13" viewBox="0 0 13 13" aria-hidden="true"><path d="M2 11l9-9M7 2h4v4M6 11H2V7" fill="none" stroke="#111" stroke-width="1.7"/></svg></div>
    </div>
  </div>

  <p class="vision-text abs">Lorem ipsum dolor sit amet, consectetur adipiscing elit. Vivamus tincidunt sapien et elit gravida tempus. Nulla blandit dolor scelerisque, elementum neque at, tincidunt nunc. Nullam volutpat auctor quam vitae tempus. Fusce tempus efficitur feugiat. Morbi iaculis ipsum ac nisi pharetra viverra vel a mi. Vivamus porta at urna a eleifend.</p>
</section>

</body>
</html>
```